Uprising SaaS company needs an attractive business card design

We're an uprising SaaS company who's attempting to attack the rigid car (insurance) claims management market in Europe.
We want to our mighty base order management system, listen to our clients to connect the smart ideas to build something even mightier.
We primarily focus on helping our customers manage their customers' claims/orders and get them resolved as smoothly as possible.
We'd like the business card design to express technical innovation and the fact that we connect smart ideas, as our company slogan indicates.
Contact Information for Business Card
Name, position, website, email, mobile, business address
Font styles to use
Colors
Designer to choose colors to be used in the design.
Look and feel
Each slider illustrates characteristics of the customer's brand and the style your logo design should communicate.

```html
<!DOCTYPE html>
<html lang="en">
<head>
<meta charset="utf-8">
<title>Nexlinka business card</title>
<link rel="stylesheet" href="https://fonts.googleapis.com/css2?family=Arimo:wght@400;700&display=swap">
<style>
  :root {
    --bg: #2a2a2a;
    --card: #121212;
    --card-edge: #1c1c1c;
    --text: #ffffff;
    --muted: #8c8c8c;
    --accent: #6ec6e0;
    --rule: #4a4a4a;
  }
  * { margin: 0; padding: 0; box-sizing: border-box; }
  html, body {
    width: 1200px;
    height: 900px;
    overflow: hidden;
    background: radial-gradient(ellipse at 50% 40%, #3a3a3a 0%, var(--bg) 55%, #161616 100%);
    font-family: "Arimo", Arial, sans-serif;
  }
  .sheet {
    position: relative;
    width: 1200px;
    height: 900px;
  }
  .card {
    position: absolute;
    top: 300px;
    width: 520px;
    height: 300px;
    border-radius: 22px;
    background: linear-gradient(160deg, var(--card-edge) 0%, var(--card) 60%, #0c0c0c 100%);
    box-shadow: 0 18px 40px rgba(0,0,0,.55);
    overflow: hidden;
  }
  .card--front { left: 50px; }
  .card--back { left: 630px; }

  .brand {
    font-family: "Arimo", Arial, sans-serif;
    font-weight: 400;
    letter-spacing: 1px;
  }
  .card--front .brand {
    position: absolute;
    left: 44px;
    top: 150px;
    font-size: 44px;
    color: var(--muted);
  }
  .card--back .brand {
    position: absolute;
    left: 0;
    right: 0;
    top: 118px;
    text-align: center;
    font-size: 52px;
    color: var(--text);
  }

  .divider {
    position: absolute;
    left: 262px;
    top: 60px;
    width: 1px;
    height: 190px;
    background: var(--rule);
  }

  .details {
    position: absolute;
    left: 286px;
    top: 62px;
    color: var(--text);
  }
  .details__name {
    font-weight: 700;
    font-size: 21px;
    color: var(--muted);
    line-height: 1.1;
  }
  .details__name .surname { color: var(--accent); }
  .details__role {
    font-size: 15px;
    margin-top: 3px;
  }
  .contact-list {
    list-style: none;
    margin-top: 14px;
  }
  .contact-list li {
    display: flex;
    align-items: center;
    gap: 8px;
    font-size: 15px;
    line-height: 23px;
  }
  .contact-list svg { width: 14px; height: 14px; flex: none; }
  .contact-list .highlight { color: var(--accent); }
  .address {
    font-style: normal;
    font-size: 15px;
    line-height: 20px;
    margin-top: 12px;
    padding-left: 22px;
  }
</style>
</head>
<body>
<main class="sheet">
  <section class="card card--front" aria-label="Card front">
    <div class="brand">nexlinka</div>
    <div class="divider"></div>
    <div class="details">
      <p class="details__name">Daniel <span class="surname">Rowe</span></p>
      <p class="details__role">Managing Director</p>
      <ul class="contact-list">
        <li>
          <svg viewBox="0 0 16 16" aria-hidden="true"><path fill="var(--accent)" d="M3.6 1.5l2.3 2.6-1.3 1.8c.9 2 2.6 3.7 4.6 4.6l1.8-1.3 2.6 2.3-1.3 2.4C6.9 13.6 2.4 9.1 1.1 2.8z"/></svg>
          <span>031-555 274 610</span>
        </li>
        <li>
          <svg viewBox="0 0 16 16" aria-hidden="true"><rect x="1" y="3" width="14" height="10" fill="var(--accent)"/><path d="M1 3l7 6 7-6" fill="none" stroke="var(--card)" stroke-width="1.3"/></svg>
          <span>hello@nexlinka.com</span>
        </li>
        <li>
          <svg viewBox="0 0 16 16" aria-hidden="true"><g fill="none" stroke="var(--accent)" stroke-width="1.4"><circle cx="8" cy="8" r="6.3"/><ellipse cx="8" cy="8" rx="2.7" ry="6.3"/><path d="M1.7 8h12.6M2.8 4.8h10.4M2.8 11.2h10.4"/></g></svg>
          <span>www.<span class="highlight">nexlinka</span>.com</span>
        </li>
      </ul>
      <address class="address">18, Harbour Lane, Suite 4<br>20314,Netherlands</address>
    </div>
  </section>

  <section class="card card--back" aria-label="Card back">
    <div class="brand">nexlinka</div>
  </section>
</main>
</body>
</html>
```